Business Card Design Project

We need a business card design for a consultancy called 'Maple Ridge'. The design should communicate innovation and professionalism. The colors used should complement our logo. Please include source files for winning design.
Updates

Industry/Entity Type

Business

Colors

Designer to choose colors to be used in the design.

Requirements
Must have
• Card size should be 85mm x 50mm. The back side of the card should be the logo on a black background. The front side should display the name 'Maple Ridge' along with standard information. The front's design should graphically complement the back.
Nice to have
• Any graphical elements in the front the complement the back side (with the logo on a black background) would be a plus.

```html
<!DOCTYPE html>
<html lang="en">
<head>
<meta charset="utf-8">
<title>Maple Ridge – Business Card</title>
<link href="https://fonts.googleapis.com/css2?family=Open+Sans:wght@400;600&display=swap" rel="stylesheet">
<style>
  :root {
    --page: #b9babd;
    --card-light: #ececec;
    --tile-light: #f3f3f3;
    --ink: #111111;
    --black: #0b0b0b;
    --white: #ffffff;
    --rule-dark: #4a4a4a;
    --rule-light: #d2d2d2;
    --brand-brown: #7a4a1c;
    --brand-amber: #e9a640;
  }
  * { margin: 0; padding: 0; box-sizing: border-box; }
  html, body {
    width: 1080px; height: 1200px; overflow: hidden;
    background: var(--page);
    font-family: "Open Sans", Arial, sans-serif;
  }
  .canvas { position: relative; width: 1080px; height: 1200px; }

  .card {
    position: absolute; left: 225px; width: 630px; height: 378px; overflow: hidden;
  }
  .card--front { top: 218px; background: linear-gradient(180deg, #f2f2f2 0%, var(--card-light) 100%); }
  .card--back { top: 709px; background: var(--black); }

  /* front: name block */
  .holder {
    position: absolute; left: 36px; top: 70px;
    color: var(--ink); white-space: nowrap;
  }
  .holder__name { font-size: 18px; }
  .holder__sep { font-size: 15px; color: #777; margin: 0 4px; }
  .holder__role { font-size: 14px; }

  .rule { position: absolute; left: 0; height: 2px; }
  .rule__short { position: absolute; left: 0; top: 0; width: 55px; height: 2px; background: var(--rule-dark); }
  .rule__long { position: absolute; left: 55px; top: 0; right: 0; height: 2px; background: var(--rule-light); }
  .card--front .rule--top { top: 102px; width: 252px; }
  .card--front .rule--bottom { top: 335px; width: 630px; }
  .card--front .rule--bottom .rule__long { background: #fafafa; }
  .card--back .rule--bottom { top: 335px; width: 632px; }
  .card--back .rule--bottom .rule__short { background: #2a2a2a; }
  .card--back .rule--bottom .rule__long { background: #e6e6e6; }

  /* front: brand */
  .brand-front { position: absolute; left: 40px; top: 144px; width: 216px; text-align: center; }
  .brand-front__disc {
    display: block; margin: 0 auto; width: 132px; height: 132px; border-radius: 50%;
    background: var(--brand-amber);
  }
  .brand-front__name {
    margin-top: 8px; font-size: 29px; font-weight: 600; letter-spacing: 1px;
    color: var(--brand-brown); white-space: nowrap;
  }

  /* front: contact tiles */
  .tile {
    position: absolute; display: flex; flex-direction: column; align-items: center; justify-content: center;
    gap: 14px; font-size: 13px; text-align: center;
  }
  .tile--dark { background: var(--black); color: var(--white); }
  .tile--light { background: var(--tile-light); color: var(--ink); }
  .tile--phone { left: 270px; top: 46px; width: 157px; height: 132px; }
  .tile--mail { left: 437px; top: 46px; width: 193px; height: 132px; }
  .tile--web { left: 270px; top: 185px; width: 157px; height: 143px; }
  .tile--address { left: 437px; top: 185px; width: 193px; height: 143px; }
  .tile svg { width: 30px; height: 30px; }

  /* back: brand */
  .brand-back { position: absolute; left: 0; right: 0; top: 98px; text-align: center; }
  .brand-back__ring {
    display: block; margin: 0 auto; width: 150px; height: 150px; border-radius: 50%;
    border: 5px solid var(--white);
  }
  .brand-back__name {
    margin-top: 8px; font-size: 34px; font-weight: 600; letter-spacing: 1.5px;
    color: var(--white); white-space: nowrap;
  }
</style>
</head>
<body>
<main class="canvas">

  <section class="card card--front" aria-label="Business card front">
    <p class="holder">
      <span class="holder__name">Name here</span><span class="holder__sep">|</span><span class="holder__role">Managing Director</span>
    </p>
    <div class="rule rule--top"><span class="rule__short"></span><span class="rule__long"></span></div>

    <div class="brand-front">
      <span class="brand-front__disc"></span>
      <p class="brand-front__name">MAPLE RIDGE</p>
    </div>

    <div class="tile tile--dark tile--phone">
      <svg viewBox="0 0 24 24" aria-hidden="true"><path fill="currentColor" d="M6.6 10.8a15.2 15.2 0 0 0 6.6 6.6l2.2-2.2c.3-.3.7-.4 1-.2 1.1.4 2.3.6 3.6.6.6 0 1 .4 1 1V20c0 .6-.4 1-1 1A17 17 0 0 1 3 4c0-.6.4-1 1-1h3.5c.6 0 1 .4 1 1 0 1.3.2 2.5.6 3.6.1.3 0 .7-.2 1z"/></svg>
      <span>(555) 010. 4821</span>
    </div>

    <div class="tile tile--light tile--mail">
      <svg viewBox="0 0 24 24" aria-hidden="true"><path fill="currentColor" d="M2 5h20v2l-10 6L2 7z"/><path fill="currentColor" d="M2 9l10 6 10-6v10H2z"/></svg>
      <span>hello@mapleridge.com</span>
    </div>

    <div class="tile tile--light tile--web">
      <svg viewBox="0 0 24 24" aria-hidden="true"><circle cx="12" cy="12" r="10" fill="none" stroke="currentColor" stroke-width="2"/><path fill="currentColor" d="M8 6c2 0 3 1 3 2s-2 1-2 3 2 2 2 4-1 3-2 3c-1-2-1-4-2-5s-2-2-2-3 1-4 3-4zm7 1c1 1 3 2 3 4s-1 1-2 2-1 3-2 3-1-2-1-3 1-2 0-3-1-2 2-3z"/></svg>
      <span>www.mapleridge.com</span>
    </div>

    <div class="tile tile--dark tile--address">
      <svg viewBox="0 0 24 24" aria-hidden="true"><path fill="currentColor" d="M12 1a7 7 0 0 0-7 7c0 5 7 15 7 15s7-10 7-15a7 7 0 0 0-7-7zm0 9.5A2.5 2.5 0 1 1 12 5.5a2.5 2.5 0 0 1 0 5z"/></svg>
      <span>Address. comes here</span>
    </div>

    <div class="rule rule--bottom"><span class="rule__short"></span><span class="rule__long"></span></div>
  </section>

  <section class="card card--back" aria-label="Business card back">
    <div class="brand-back">
      <span class="brand-back__ring"></span>
      <p class="brand-back__name">MAPLE RIDGE</p>
    </div>
    <div class="rule rule--bottom"><span class="rule__short"></span><span class="rule__long"></span></div>
  </section>

</main>
</body>
</html>
```